Marwick Estate Services (Handyman / Home Improvement Company)

Looking for a double sided professional looking business card with Logo attached to be highlighted on one side and throwing in an image of a handyman as an option would be nice to see as well. We are a company focused on providing quality Handyman and Home improvement services in a timely manner that is done right the first time with integrity

Industry/Entity Type

Handyman / Home Improvement

Contact Information for Business Card

(LOGO, Name, Mobile and office phone numbers, email) on front side of card, (the words "The SOLUTION to all of your Handyman and Home Improvement needs" followed by "Family Owned and Operated" at the very bottom) on the back.

Colors
EB3D1F
EC4F4E
F09395
F8D3D4
FCEDEE

Requirements
Must have
• Red, Gray, Black Color scheme
Should not have
• No Yellow or Blue colors

```html
<!DOCTYPE html>
<html lang="en">
<head>
<meta charset="utf-8">
<title>Marwick Estate Services – Business Card</title>
<link rel="stylesheet" href="https://fonts.googleapis.com/css2?family=Montserrat:wght@400;500;600;700&display=swap">
<style>
  :root {
    --brand-red: #e92d30;
    --ink: #111111;
    --paper: #ffffff;
    --canvas: #ffffff;
    --shadow: rgba(0, 0, 0, 0.28);
  }
  * { margin: 0; padding: 0; box-sizing: border-box; }
  html, body { width: 1200px; height: 1200px; overflow: hidden; background: var(--canvas); }
  body { position: relative; font-family: "Montserrat", sans-serif; color: var(--ink); }

  .card {
    position: absolute;
    left: 266px;
    width: 676px;
    height: 386px;
    box-shadow: 0 26px 30px -8px var(--shadow), 0 4px 18px rgba(0,0,0,0.08);
    overflow: hidden;
  }
  .card--front { top: 130px; background: var(--paper); }
  .card--back { top: 662px; background: var(--brand-red); }

  /* Front side */
  .brand-name {
    position: absolute;
    display: flex;
    align-items: center;
    gap: 10px;
    font-weight: 700;
    text-transform: uppercase;
    line-height: 1.05;
  }
  .card--front .brand-name {
    left: 330px; top: 80px; width: 290px;
    font-size: 27px; color: var(--brand-red);
  }
  .brand-mark {
    flex: none;
    width: 18px; height: 18px;
    border-radius: 50%;
    background: currentColor;
  }
  .holder-name {
    position: absolute;
    left: 70px; top: 190px;
    font-size: 31px; font-weight: 500;
    letter-spacing: 0.5px;
  }
  .holder-title {
    position: absolute;
    left: 71px; top: 231px;
    font-size: 11px; font-weight: 500;
    color: var(--brand-red);
    letter-spacing: 0.5px;
  }
  .divider {
    position: absolute;
    left: 70px; top: 255px;
    width: 536px; height: 2px;
    background: var(--ink);
  }
  .contact-list { list-style: none; }
  .contact-item {
    position: absolute;
    display: flex; align-items: center; gap: 14px;
    font-size: 19px; font-weight: 500;
    letter-spacing: 0.3px;
  }
  .contact-item svg { width: 24px; height: 24px; flex: none; }
  .contact-item--phone { left: 68px; top: 278px; }
  .contact-item--office { left: 68px; top: 320px; }
  .contact-item--email { left: 351px; top: 278px; }
  .contact-item--web { left: 351px; top: 320px; }

  /* Back side */
  .card--back .brand-name {
    left: 0; right: 0; top: 80px;
    justify-content: center;
    font-size: 32px; color: var(--paper);
    text-align: center;
  }
  .card--back .brand-name span { max-width: 300px; }
  .tagline {
    position: absolute;
    left: 0; right: 0; top: 262px;
    text-align: center;
    color: var(--paper);
    font-size: 18px; font-weight: 500;
    text-transform: uppercase;
    line-height: 23px;
    letter-spacing: 0.6px;
  }
  .tagline strong { font-size: 24px; font-weight: 500; }
  .band {
    position: absolute;
    top: 330px; height: 13px;
    background: var(--paper);
  }
  .band--left { left: 0; width: 161px; }
  .band--right { right: 0; width: 161px; }
  .ownership {
    position: absolute;
    left: 0; right: 0; top: 325px;
    text-align: center;
    color: var(--paper);
    font-size: 19px; font-weight: 500;
    letter-spacing: 0.6px;
  }
</style>
</head>
<body>

<section class="card card--front" aria-label="Business card front">
  <div class="brand-name"><i class="brand-mark"></i><span>Marwick Estate Services</span></div>

  <h1 class="holder-name">YOUR NAME</h1>
  <p class="holder-title">TITLE</p>
  <div class="divider"></div>

  <ul class="contact-list">
    <li class="contact-item contact-item--phone">
      <svg viewBox="0 0 24 24" aria-hidden="true"><circle cx="12" cy="12" r="12" fill="var(--brand-red)"/><path d="M8 6.5l2 2.5-1.2 1.5c.8 1.8 2 3 3.8 3.8L14 13l2.5 2-1 2c-4.5-.3-8.3-4.1-8.6-8.6z" fill="#fff"/></svg>
      Your Phone Number
    </li>
    <li class="contact-item contact-item--office">
      <svg viewBox="0 0 24 24" aria-hidden="true"><circle cx="12" cy="12" r="12" fill="var(--brand-red)"/><path d="M6 10c1-2 11-2 12 0v1.5h-3V10H9v1.5H6z M8 12h8l1 5H7z" fill="#fff"/></svg>
      Your Phone Office
    </li>
    <li class="contact-item contact-item--email">
      <svg viewBox="0 0 24 24" aria-hidden="true"><circle cx="12" cy="12" r="12" fill="var(--brand-red)"/><rect x="6.5" y="8" width="11" height="8" fill="none" stroke="#fff" stroke-width="1.4"/><path d="M6.5 8l5.5 4.5L17.5 8" fill="none" stroke="#fff" stroke-width="1.4"/></svg>
      Your Business Email
    </li>
    <li class="contact-item contact-item--web">
      <svg viewBox="0 0 24 24" aria-hidden="true"><circle cx="12" cy="12" r="12" fill="var(--brand-red)"/><g fill="none" stroke="#fff" stroke-width="1.3"><circle cx="12" cy="12" r="6"/><ellipse cx="12" cy="12" rx="2.6" ry="6"/><path d="M6 12h12M7 9h10M7 15h10"/></g></svg>
      Your Business Website
    </li>
  </ul>
</section>

<section class="card card--back" aria-label="Business card back">
  <div class="brand-name"><i class="brand-mark"></i><span>Marwick Estate Services</span></div>

  <p class="tagline">Your <strong>Solution</strong> to all of your handyman and<br>home improvement needs</p>

  <div class="band band--left"></div>
  <div class="band band--right"></div>
  <p class="ownership">FAMILY OWNED AND OPERATED</p>
</section>

</body>
</html>
```